New Business Card Design for Engineering and Surveying Company

We need a new design template for our business cards. We are a civil engineering, land surveying and pipeline integrity business. Please see dkhpartners.com for details. We need a bold, new business card design to complement our rebranding and marketing program. We have anew logo and attached vectro file. Please find additional details below. I am available to answer any questions.

Target Market(s)

Contractors, business owners, oil companies

Contact Information for Business Card

Needs to be customizable for different people (name, title, cell)

Font styles to use
Sans Serif
Other font styles liked:
• See eps file

Requirements
Must have
• Example Information:
Trevor Ashcombe

T:409-555-0173
M: 202-555-0148
tashcombe@dkhprtnrs.com

Address: 1875 Pinecrest Parkway, Beaumont, Texas 77703
Email: tolvanrey@dkhpartners.com
Website: www.dkhpartners.com
Nice to have
• I would like the back of the card to have the logo on a bold background with the text below:

[logo]
DORAN KESSLING & PARTNERS
CIVIL ENGINEERING | LAND SURVEYING | PIPELINE INTEGRITY

The reverse side should have the contact information for the person (example above), a smaller version of the logo and a graphic

```html
<!DOCTYPE html>
<html lang="en">
<head>
<meta charset="utf-8">
<title>Doran Kessling &amp; Partners – Business Card</title>
<link rel="stylesheet" href="https://fonts.googleapis.com/css2?family=Roboto:wght@400;500;700;900&display=swap">
<style>
  :root {
    --backdrop: #d9d8d5;
    --card: #05080f;
    --card-edge: #141a26;
    --white: #ffffff;
    --text-light: #e6e8ec;
    --red: #ed1b2f;
    --blue: #2456b3;
    --divider: #3a414d;
  }
  * { margin: 0; padding: 0; box-sizing: border-box; }
  html, body {
    width: 1200px; height: 801px; overflow: hidden;
    background: var(--backdrop);
    font-family: "Roboto", Arial, sans-serif;
  }
  .sheet {
    width: 1200px; height: 801px;
    display: flex; align-items: center; justify-content: center; gap: 40px;
  }
  .card {
    position: relative;
    width: 540px; height: 309px;
    background: linear-gradient(145deg, #0c111b 0%, var(--card) 60%);
    border: 1px solid var(--card-edge);
    overflow: hidden;
  }

  /* Contact side */
  .card-contact .brand {
    position: absolute; left: 0; top: 0; width: 230px; height: 100%;
    display: flex; align-items: center; justify-content: center; gap: 10px;
  }
  .brand-mark { width: 14px; height: 14px; background: var(--red); }
  .brand-name {
    color: var(--white); font-weight: 900; font-size: 46px; letter-spacing: 2px;
  }
  .card-contact .divider {
    position: absolute; left: 230px; top: 40px; width: 1px; height: 229px;
    background: linear-gradient(to bottom, transparent, var(--divider) 30%, var(--divider) 70%, transparent);
  }
  .details {
    position: absolute; left: 256px; top: 48px; right: 20px;
    color: var(--text-light); font-size: 13px; line-height: 1.45;
  }
  .person-name {
    color: var(--red); font-weight: 700; font-size: 20px; letter-spacing: .5px;
    text-transform: uppercase; line-height: 1.1;
  }
  .person-title { color: var(--blue); font-weight: 500; font-size: 15px; margin-bottom: 8px; }
  .address { margin-bottom: 4px; }
  .contact-line { display: flex; align-items: center; gap: 7px; }
  .contact-line svg { width: 13px; height: 13px; flex: none; }

  /* Brand side */
  .card-brand {
    display: flex; flex-direction: column; align-items: center; justify-content: center;
  }
  .card-brand .brand-lockup { display: flex; align-items: center; gap: 16px; margin-bottom: 22px; }
  .card-brand .brand-mark { width: 24px; height: 24px; }
  .card-brand .brand-name { font-size: 92px; letter-spacing: 4px; line-height: 1; }
  .company-name {
    color: var(--text-light); font-weight: 500; font-size: 15px; letter-spacing: 1px; margin-bottom: 8px;
  }
  .services {
    display: flex; align-items: center; gap: 12px;
    color: var(--text-light); font-weight: 500; font-size: 12.5px; letter-spacing: .8px;
    white-space: nowrap;
  }
  .service-dash { width: 24px; height: 7px; background: var(--red); transform: skewX(-40deg); }
</style>
</head>
<body>
<main class="sheet">

  <section class="card card-contact" aria-label="Business card, contact side">
    <div class="brand">
      <span class="brand-mark"></span>
      <span class="brand-name">DKP</span>
    </div>
    <div class="divider"></div>
    <div class="details">
      <p class="person-name">Trevor Ashcombe</p>
      <p class="person-title">Director</p>
      <p class="address">1875 Pinecrest Parkway,<br>Cedar Hollow, Texas 77590</p>
      <p class="contact-line">
        <svg viewBox="0 0 14 14" aria-hidden="true"><rect x="3.5" y="1" width="7" height="12" rx="1.2" fill="none" stroke="var(--red)" stroke-width="1.4"/><circle cx="7" cy="11" r=".8" fill="var(--red)"/></svg>
        202-555-0148
      </p>
      <p class="contact-line">
        <svg viewBox="0 0 14 14" aria-hidden="true"><path d="M1 5c0-2 2.5-3 6-3s6 1 6 3v1H10V4.5H4V6H1z" fill="var(--red)"/><rect x="2.5" y="7" width="9" height="6" rx="1" fill="var(--red)"/></svg>
        409-555-0173
      </p>
      <p class="contact-line">
        <svg viewBox="0 0 14 14" aria-hidden="true"><rect x="1" y="3" width="12" height="8" fill="var(--red)"/><path d="M1 3l6 5 6-5" fill="none" stroke="var(--card)" stroke-width="1"/></svg>
        tashcombe@dkhprtnrs.com
      </p>
      <p class="contact-line">
        <svg viewBox="0 0 14 14" aria-hidden="true"><circle cx="7" cy="7" r="6" fill="var(--red)"/><path d="M1 7h12M7 1c-2.5 3-2.5 9 0 12M7 1c2.5 3 2.5 9 0 12" fill="none" stroke="var(--card)" stroke-width=".8"/></svg>
        www.dkhpartners.com
      </p>
    </div>
  </section>

  <section class="card card-brand" aria-label="Business card, brand side">
    <div class="brand-lockup">
      <span class="brand-mark"></span>
      <span class="brand-name">DKP</span>
    </div>
    <p class="company-name">DORAN KESSLING &amp; PARTNERS</p>
    <p class="services">
      <span class="service-dash"></span>CIVIL ENGINEERING
      <span class="service-dash"></span>LAND SURVEYING
      <span class="service-dash"></span>PIPELINE INTEGRITY
    </p>
  </section>

</main>
</body>
</html>
```